Unique Flyer Project - www.plumvaleforms.com.au

The purpose of this flyer is trying to get recipients to visit the website www.plumvaleforms.com.au and sign up to the offer. I need it to be simple/to the point, eye catching and professional. I will post up a basic idea I have but feel free to put your own spin on it if you think you have great ideas to get people to visit the site, if not then just improve upon the quality of mine and make it look like a respected company.

I also think a red band or something that REALLY catches the eye highlighting one of the important aspects of the flyer (the domain?) could be great so even if someone is about to put it in the bin, the popping red-on-white-background catches their eye so they end up looking at and reading the flyer.

I would also love a VERY SIMPLE design for the backside of the flyer, just a red box/band (whatever you think is good) with the domain 'www.plumvaleforms.com.au' in it. NOTHING ELSE! Just so if it's floating around the table and it's upside down, there's something eye catching that might entice the householder to look at it.

DESIGN IS FOR DL FLYER: 99mm X 210mm

Target Market(s)

Australian Residents interested in earning money from home.

Industry/Entity Type

It Company

Requirements
Must have
• Eye catching (mainly red band/box/bar on front & back page), SIMPLE, elegant/professional.
Should not have
• ANYTHING unnecessary to the reader that will distract them from the ultimate point - GET PAID TO DO SURVEYS FROM YOUR OWN HOME ON THE COMPUTER!

```html
<!DOCTYPE html>
<html lang="en">
<head>
<meta charset="utf-8">
<title>Plumvale Forms – DL Flyer</title>
<link rel="stylesheet" href="https://fonts.googleapis.com/css2?family=Source+Sans+3:wght@300;400;700;900&display=swap">
<style>
  :root {
    --backdrop: #e6e4e1;
    --paper: #ffffff;
    --band-red: #d3121c;
    --band-red-dark: #a80d14;
    --band-red-light: #e8363d;
    --brand-blue: #1a5f99;
    --ink-grey: #666a6e;
    --ink-dark: #2a2a2a;
    --card-shadow: 0 6px 18px rgba(0,0,0,.22);
  }
  * { box-sizing: border-box; margin: 0; padding: 0; }
  html, body {
    width: 1200px; height: 803px; overflow: hidden;
    background: var(--backdrop);
    font-family: "Source Sans 3", "Source Sans Pro", Arial, sans-serif;
  }
  .canvas { position: relative; width: 1200px; height: 803px; }

  .flyer {
    position: absolute;
    background: var(--paper);
    box-shadow: var(--card-shadow);
    overflow: hidden;
  }
  .band {
    position: absolute; left: 0; right: 0;
    display: flex; align-items: center; justify-content: center;
    background: linear-gradient(180deg, var(--band-red-light) 0%, var(--band-red) 45%, var(--band-red-dark) 100%);
    border-top: 2px solid rgba(255,255,255,.6);
    border-bottom: 3px solid rgba(90,0,0,.35);
    color: #fff;
    white-space: nowrap;
  }
  .domain-light { font-weight: 300; letter-spacing: .5px; }
  .domain-bold { font-weight: 700; }

  /* back variants */
  .back-plain { left: 22px; top: 14px; width: 560px; height: 278px; }
  .back-plain .band { top: 168px; height: 66px; font-size: 36px; }

  .back-reflect { left: 618px; top: 14px; width: 562px; height: 280px; }
  .back-reflect .band { top: 118px; height: 80px; flex-direction: column; font-size: 25px; line-height: 1; }
  .back-reflect .mirror { transform: scaleY(-1); opacity: .45; margin-top: 2px; }

  .back-minimal { left: 18px; top: 492px; width: 562px; height: 292px; }
  .back-minimal .domain { position: absolute; top: 126px; width: 100%; text-align: center; font-size: 25px; color: var(--brand-blue); }

  .back-band { left: 620px; top: 486px; width: 562px; height: 300px; }
  .back-band .band { top: 106px; height: 90px; font-size: 25px; }

  /* front */
  .front { left: 308px; top: 246px; width: 572px; height: 284px; z-index: 2; box-shadow: 0 10px 26px rgba(0,0,0,.35); }
  .front p, .front h1 { line-height: 1; white-space: nowrap; }
  .front .question { position: absolute; left: 28px; top: 16px; font-size: 28px; font-weight: 300; color: var(--ink-grey); }
  .front .brand {
    position: absolute; right: 20px; top: 40px;
    display: flex; align-items: center; gap: 5px;
    font-size: 15px; font-weight: 700; color: var(--brand-blue);
  }
  .front .brand-dot { width: 10px; height: 10px; background: var(--band-red); border-radius: 50%; }
  .front .headline { position: absolute; left: 22px; top: 56px; font-size: 40px; font-weight: 900; color: var(--brand-blue); letter-spacing: -1px; }
  .front .amount {
    position: absolute; left: 262px; top: 102px;
    display: flex; align-items: flex-start;
    color: var(--brand-blue); font-weight: 900;
  }
  .front .amount .currency { font-size: 34px; font-weight: 400; margin-top: 18px; margin-right: 2px; }
  .front .amount .figure { font-size: 68px; letter-spacing: -2px; }
  .front .per-survey { position: absolute; left: 374px; top: 130px; font-size: 36px; font-weight: 900; color: var(--brand-blue); letter-spacing: -1px; }
  .front .band { top: 176px; height: 56px; font-size: 38px; }
  .front .tagline { position: absolute; top: 250px; width: 100%; text-align: center; font-size: 16px; color: var(--ink-dark); }
</style>
</head>
<body>
<main class="canvas">

  <section class="flyer back-plain" aria-label="Flyer back, plain band">
    <div class="band"><span class="domain-light">www.plumvaleforms.com.au</span></div>
  </section>

  <section class="flyer back-reflect" aria-label="Flyer back, band with reflection">
    <div class="band">
      <span class="domain-bold">www.plumvaleforms.com.au</span>
      <span class="domain-bold mirror" aria-hidden="true">www.plumvaleforms.com.au</span>
    </div>
  </section>

  <section class="flyer back-minimal" aria-label="Flyer back, domain only">
    <p class="domain domain-bold">www.plumvaleforms.com.au</p>
  </section>

  <section class="flyer back-band" aria-label="Flyer back, wide band">
    <div class="band"><span class="domain-bold">www.plumvaleforms.com.au</span></div>
  </section>

  <section class="flyer front" aria-label="Flyer front">
    <p class="question">Could you use an extra income?</p>
    <div class="brand"><span class="brand-dot"></span><span>Plumvale Forms</span></div>
    <h1 class="headline">Earn as much as</h1>
    <p class="amount"><span class="currency">$</span><span class="figure">50</span></p>
    <p class="per-survey">per survey!</p>
    <div class="band"><span class="domain-light">www.plumvaleforms.com.au</span></div>
    <p class="tagline">Work from home and choose your own hours!</p>
  </section>

</main>
</body>
</html>
```